Tallowreed Advisory Partners Business Card Design

We have the logo we just need someone to design a modern business card design.

Name: Desmond Munkalt
Phone: 3055550148
Mobile: 9175550193
Web:www.tallowreedadvisory.example
email: dmunkalt@tallowreedadvisory.example
Company: Tallowreed Advisory Partners
Title: CEO

Address: 718 Quillmore Ave, Miami, Florida 33190

Target Market(s)

companies over 100 employees

Industry/Entity Type

Business

```html
<!DOCTYPE html>
<html lang="en">
<head>
<meta charset="utf-8">
<title>Tallowreed Advisory Partners – Business Card</title>
<link rel="stylesheet" href="https://fonts.googleapis.com/css2?family=Arimo:wght@400;700&display=swap">
<style>
  :root {
    --backdrop: #e4e5e7;
    --card: #ffffff;
    --brand-blue: #3f63b3;
    --ink: #111111;
    --text-grey: #3a3a3a;
    --rule: #9a9a9a;
  }
  * { margin: 0; padding: 0; box-sizing: border-box; }
  html, body {
    width: 1200px; height: 720px; overflow: hidden;
    background: var(--backdrop);
    font-family: "Arimo", Arial, sans-serif;
  }
  .stage { position: relative; width: 1200px; height: 720px; }
  .card {
    position: absolute; top: 237px;
    width: 486px; height: 281px;
    background: var(--card);
    border-radius: 14px;
  }
  .card--front { left: 80px; }
  .card--back { left: 629px; }
  .abs { position: absolute; white-space: nowrap; }
  .brand-dot { position: absolute; border-radius: 50%; background: var(--brand-blue); }
  .brand-name {
    position: absolute; right: 16px; text-align: right;
    color: var(--ink); font-weight: 700; line-height: 1;
  }
  .brand-name .main { display: block; font-size: 21px; letter-spacing: 1px; }
  .brand-name .sub { display: block; font-size: 7.5px; letter-spacing: 0.6px; margin-top: 3px; }

  .person { right: 16px; top: 164px; text-align: right; }
  .person__name { color: var(--brand-blue); font-size: 14.5px; }
  .person__rule {
    position: absolute; left: 105px; top: 188px; width: 340px; height: 1px;
    background: linear-gradient(to right, rgba(154,154,154,0), var(--rule));
  }
  .person__title { right: 16px; top: 180px; font-size: 11px; color: var(--ink); }

  .contacts { right: 18px; top: 207px; text-align: right; list-style: none; }
  .contacts li {
    font-size: 11px; color: var(--text-grey); height: 14.5px; line-height: 14.5px;
    display: flex; justify-content: flex-end; align-items: center; gap: 4px;
  }
  .contacts svg { width: 11px; height: 11px; fill: none; stroke: var(--brand-blue); stroke-width: 1.6; }
  .contacts .icon-solid { fill: var(--brand-blue); stroke: none; }

  .address { left: 19px; top: 222px; font-size: 11px; color: var(--text-grey); line-height: 14.5px; }
  .address strong { font-weight: 700; }

  .back-web { right: 18px; top: 223px; font-size: 11px; font-weight: 700; color: var(--text-grey); }
</style>
</head>
<body>
<main class="stage">
  <section class="card card--front" aria-label="Card front">
    <span class="brand-dot" style="left:346px; top:19px; width:70px; height:70px;"></span>
    <div class="brand-name" style="top:101px;">
      <span class="main">TALLOWREED</span>
      <span class="sub">ADVISORY PARTNERS</span>
    </div>

    <div class="abs person"><span class="person__name">Desmond Munkalt</span></div>
    <span class="person__rule"></span>
    <div class="abs person__title">CEO</div>

    <ul class="abs contacts">
      <li>3055550148
        <svg viewBox="0 0 12 12"><path class="icon-solid" d="M1 4.5C1 3 3 2 6 2s5 1 5 2.5V6H8.5V4.8h-5V6H1zM3 6.5h6l1.5 4h-9z"/></svg>
      </li>
      <li>9175550193
        <svg viewBox="0 0 12 12"><rect x="3" y="1" width="6" height="10" rx="1"/><line x1="5.5" y1="9.3" x2="6.5" y2="9.3"/></svg>
      </li>
      <li>www.tallowreedadvisory.example
        <svg viewBox="0 0 12 12"><rect x="1" y="1.5" width="10" height="7"/><line x1="4" y1="10.5" x2="8" y2="10.5"/></svg>
      </li>
      <li style="padding-right:15px;">dmunkalt@tallowreedadvisory.example</li>
    </ul>

    <address class="abs address" style="font-style:normal;">
      <strong>Tallowreed Advisory Partners</strong><br>
      718 Quillmore Ave<br>
      Miami, Florida 33190
    </address>
  </section>

  <section class="card card--back" aria-label="Card back">
    <span class="brand-dot" style="left:20px; top:19px; width:102px; height:102px;"></span>
    <div class="brand-name" style="top:184px;">
      <span class="main">TALLOWREED</span>
      <span class="sub">ADVISORY PARTNERS</span>
    </div>
    <div class="abs back-web">www.tallowreedadvisory.example</div>
  </section>
</main>
</body>
</html>
```